Business card and stationery design

Harbour & Summit Planners is a leading event and conference design and management company.
Please view harbourandsummit.com.au

The business cards needs to convey:
- professionalism and competency
- exclusivity
- memorable experiences and quality

The business card needs to have the following aspects:
- double sided
- Full colour CMYK
- Printed on either high gloss matt card (designer to recommend)

For the business stationery we require:
- Letterhead with top banner and bottom footer
- A thank you card design
- a with compliments slip design
- a MS powerpoint and MS publisher client presentation slide design which includes cover page and then a standard presentation page
(Note- we do NOT require an envelope design- who sends letters these days!)

The company image is using the key colours of gold, silver and black.
A black background to the business card has been used before and is preferred although we are open to options.

Target Market(s)

High end corporations and businesses that require their events and conferences to be exceptionally well designed and managed

Industry/Entity Type

Business

Contact Information for Business Card

FRONT:

Darcy Whitlam
- Event and Conference Specialist

Mobile- +61 (0) 491 362 047
Office- 1300 586 917
darcyw@harbourandsummit.com.au

Web- harbourandsummit.com.au

BACK:

- Event and

Font styles to use
Other font styles liked:
• The logo designer used Trajan Pro Bold 3 for the font text in the logo

Requirements
Must have
• Amazing design of the following:
• - business card (double sided)
• - letterhead
• - client thank you card
• - powerpoint and publisher client presentation design files

```html
<!DOCTYPE html>
<html lang="en">
<head>
<meta charset="utf-8">
<title>Harbour &amp; Summit Planners – Business Card</title>
<link rel="stylesheet" href="https://fonts.googleapis.com/css2?family=Open+Sans:wght@400;600;700&display=swap">
<style>
  :root {
    --backdrop: #e9e6e1;
    --card-black: #050505;
    --silver-light: #e6e6e6;
    --silver-dark: #8d8d8d;
    --gold-light: #f1e3a4;
    --gold-mid: #e2c46a;
    --gold-dark: #c6922a;
    --ink: #141414;
    --logo-silver: #e4e4e4;
    --logo-gold: #d4ad4a;
  }
  * { box-sizing: border-box; margin: 0; padding: 0; }
  html, body {
    width: 1200px; height: 900px; overflow: hidden;
    background: var(--backdrop);
    font-family: "Open Sans", Arial, sans-serif;
  }
  .business-card {
    position: absolute; left: 110px; top: 148px;
    width: 980px; height: 604px;
    background: var(--card-black);
    overflow: hidden;
    box-shadow: 0 10px 30px rgba(0,0,0,0.18);
  }
  .card-wave { position: absolute; inset: 0; width: 100%; height: 100%; }

  .brand {
    position: absolute; left: 120px; top: 232px; width: 320px;
    text-align: center; color: var(--logo-silver);
    font-weight: 600; font-size: 25px; letter-spacing: 1.5px;
    line-height: 1.2; text-transform: uppercase;
  }
  .brand-mark {
    position: absolute; left: 248px; top: 108px;
    width: 64px; height: 64px; border-radius: 50%;
    background: var(--logo-gold);
  }

  .cardholder {
    position: absolute; right: 57px; text-align: right; color: var(--ink);
  }
  .cardholder-name { top: 298px; font-size: 32px; font-weight: 700; line-height: 1.3; }
  .cardholder-title { top: 343px; font-size: 23px; font-weight: 400; line-height: 1.3; }

  .contact-list { position: absolute; right: 57px; top: 410px; list-style: none; }
  .contact-item {
    display: flex; align-items: center; justify-content: flex-end;
    height: 41px; font-size: 22px; color: var(--ink);
  }
  .contact-icon { width: 20px; height: 20px; margin-left: 14px; fill: var(--ink); }
</style>
</head>
<body>
  <article class="business-card">
    <svg class="card-wave" viewBox="0 0 652 402" preserveAspectRatio="none" aria-hidden="true">
      <defs>
        <linearGradient id="silverBand" x1="0" y1="0" x2="1" y2="0">
          <stop offset="0" stop-color="var(--silver-dark)"/>
          <stop offset="0.35" stop-color="var(--silver-light)"/>
          <stop offset="0.7" stop-color="#b5b5b5"/>
          <stop offset="1" stop-color="var(--silver-light)"/>
        </linearGradient>
        <linearGradient id="goldPanel" x1="0" y1="0" x2="0" y2="1">
          <stop offset="0.25" stop-color="var(--gold-light)"/>
          <stop offset="0.65" stop-color="var(--gold-mid)"/>
          <stop offset="1" stop-color="var(--gold-dark)"/>
        </linearGradient>
      </defs>
      <path fill="url(#silverBand)" d="M0,168 C60,232 120,282 200,282 C300,282 380,158 470,108 C540,72 612,78 652,112 L652,402 L0,402 Z"/>
      <path fill="var(--card-black)" d="M0,178 C60,240 120,292 204,292 C302,292 386,170 476,122 C546,88 612,94 652,126 L652,402 L0,402 Z"/>
      <path fill="url(#goldPanel)" d="M0,184 C60,250 126,300 210,300 C306,300 390,180 480,132 C550,98 614,104 652,134 L652,402 L0,402 Z"/>
    </svg>

    <span class="brand-mark" aria-hidden="true"></span>
    <p class="brand">Harbour &amp; Summit<br>Planners</p>

    <h1 class="cardholder cardholder-name">Darcy Whitlam</h1>
    <p class="cardholder cardholder-title">Event and Conference Specialist</p>

    <ul class="contact-list">
      <li class="contact-item">+61 (0) 491 362 047
        <svg class="contact-icon" viewBox="0 0 20 20" aria-label="Mobile"><path d="M6 1h8a1.5 1.5 0 0 1 1.5 1.5v15A1.5 1.5 0 0 1 14 19H6a1.5 1.5 0 0 1-1.5-1.5v-15A1.5 1.5 0 0 1 6 1zm0 2.5v11.5h8V3.5zm4 12.6a1 1 0 1 0 0 2 1 1 0 0 0 0-2z"/></svg>
      </li>
      <li class="contact-item">1300 586 917
        <svg class="contact-icon" viewBox="0 0 20 20" aria-label="Office phone"><path d="M4.5 1.5l3 .5 1.5 4-2 1.5a11 11 0 0 0 5.5 5.5l1.5-2 4 1.5.5 3c0 1.5-1 2.5-2.5 2.5C8.5 18 2 11.5 2 4c0-1.5 1-2.5 2.5-2.5z"/></svg>
      </li>
      <li class="contact-item">darcyw@harbourandsummit.com.au
        <svg class="contact-icon" viewBox="0 0 20 20" aria-label="Email"><path d="M2 4h16v12H2zm1.5 1.5v.4L10 10.5l6.5-4.6v-.4zm0 2.2v6.8h13V7.7L10 12.3z"/></svg>
      </li>
      <li class="contact-item">www.harbourandsummit.com.au
        <svg class="contact-icon" viewBox="0 0 20 20" aria-label="Website"><path d="M10 1.5a8.5 8.5 0 1 0 0 17 8.5 8.5 0 0 0 0-17zm-1.2 3c1 .5 1.6 1.4 1.2 2.3-.5 1-1.8.8-2.3 1.8-.4 1 .6 1.7 1.6 1.9 1.2.3 1.6 1.3 1.1 2.4-.4.9-.2 2 .4 2.8A6.5 6.5 0 0 1 4 7.2c1.5-.2 3.1-1.3 4.8-2.7zm4.7 1.4a6.5 6.5 0 0 1 2.9 6.3c-.8-.6-1.8-.6-2.4-1.4-.6-.9.2-1.9-.4-2.8-.5-.7-1.4-.5-1.7-1.3-.2-.5.7-.8 1.6-.8z"/></svg>
      </li>
    </ul>
  </article>
</body>
</html>
```